Letterhead design for business

Looking for an attractive and professional letterhead that uses the logo that is attached below.

Target Market(s)

Potential bankruptcy clients.

Industry/Entity Type

Legal

Colors

Designer to choose colors to be used in the design.

Requirements
Must have
• Address for locations, phone number, and website address.
• Addresses are on website larkmoorfirm.legal. Use following phone number (for tracking purposes): 404-731-2864

```html
<!DOCTYPE html>
<html lang="en">
<head>
<meta charset="utf-8">
<title>Larkmoor Law Group – Letterhead</title>
<link rel="stylesheet" href="https://fonts.googleapis.com/css2?family=Dosis:wght@500&family=Arimo:wght@400&display=swap">
<style>
  :root {
    --canvas-bg: #e4e4e4;
    --paper: #ffffff;
    --brand-green: #7cc08a;
    --brand-green-soft: #9fd3a8;
    --charcoal: #3d3d3f;
    --footer-text: #ffffff;
  }
  * { margin: 0; padding: 0; box-sizing: border-box; }
  html, body {
    width: 1200px;
    height: 1200px;
    overflow: hidden;
    background: var(--canvas-bg);
  }
  .letterhead {
    position: absolute;
    left: 260px;
    top: 40px;
    width: 681px;
    height: 1120px;
    background: var(--paper);
    box-shadow: 0 4px 18px rgba(0, 0, 0, 0.18);
    overflow: hidden;
  }
  .letterhead__graphics {
    position: absolute;
    inset: 0;
    width: 100%;
    height: 100%;
  }
  .brand {
    position: absolute;
    left: 0;
    right: 0;
    top: 160px;
    display: flex;
    align-items: center;
    justify-content: center;
    gap: 14px;
  }
  .brand__dot {
    width: 30px;
    height: 30px;
    border-radius: 50%;
    background: var(--brand-green);
  }
  .brand__name {
    font-family: "Dosis", sans-serif;
    font-weight: 500;
    font-size: 34px;
    color: var(--charcoal);
    letter-spacing: 0.5px;
  }
  .contact {
    position: absolute;
    top: 1074px;
    display: flex;
    align-items: center;
    gap: 11px;
    font-family: "Arimo", sans-serif;
    font-size: 13px;
    color: var(--footer-text);
  }
  .contact__icon { width: 18px; height: 18px; flex: none; }
  .contact--phone { left: 34px; }
  .contact--address { left: 222px; }
  .contact--web { left: 487px; }
</style>
</head>
<body>
  <main class="letterhead">
    <svg class="letterhead__graphics" viewBox="0 0 798 1310" preserveAspectRatio="none" aria-hidden="true">
      <!-- header -->
      <path fill="var(--charcoal)" d="M560 0 L798 0 L798 118 C740 52 650 4 560 0 Z"/>
      <path fill="var(--brand-green)" d="M0 0 L90 0 C250 58 430 12 560 6 C650 4 735 58 798 122 L798 138 C725 72 640 32 545 27 C400 22 210 64 0 64 Z"/>
      <!-- footer -->
      <path fill="var(--brand-green)" d="M0 1172 C210 1240 510 1255 798 1096 L798 1112 C560 1236 300 1248 0 1245 Z"/>
      <path fill="var(--charcoal)" d="M0 1245 C300 1248 560 1236 798 1112 L798 1310 L0 1310 Z"/>
    </svg>

    <header class="brand">
      <span class="brand__dot"></span>
      <span class="brand__name">Larkmoor Law Group</span>
    </header>

    <footer>
      <div class="contact contact--phone">
        <svg class="contact__icon" viewBox="0 0 20 20" aria-hidden="true">
          <circle cx="10" cy="10" r="8.5" fill="none" stroke="var(--brand-green)" stroke-width="1.5"/>
          <path d="M8 6 L9.2 8.4 L8.4 9.3 C8.9 10.4 9.6 11.1 10.7 11.6 L11.6 10.8 L14 12 L13.3 13.6 C10 13.6 6.4 10 6.4 6.7 Z" fill="var(--brand-green)"/>
        </svg>
        <span>404-731-2864</span>
      </div>
      <div class="contact contact--address">
        <svg class="contact__icon" viewBox="0 0 20 20" aria-hidden="true">
          <circle cx="10" cy="10" r="8.5" fill="none" stroke="var(--brand-green)" stroke-width="1.5"/>
          <path d="M10 4.5 C7.8 4.5 6.3 6.1 6.3 8.1 C6.3 10.8 10 15 10 15 C10 15 13.7 10.8 13.7 8.1 C13.7 6.1 12.2 4.5 10 4.5 Z M10 9.6 A1.5 1.5 0 1 1 10 6.6 A1.5 1.5 0 1 1 10 9.6 Z" fill="var(--brand-green)" fill-rule="evenodd"/>
        </svg>
        <span>Your Address Goes Here</span>
      </div>
      <div class="contact contact--web">
        <svg class="contact__icon" viewBox="0 0 20 20" aria-hidden="true">
          <g fill="none" stroke="var(--brand-green)" stroke-width="1.3">
            <circle cx="10" cy="10" r="8.5"/>
            <ellipse cx="10" cy="10" rx="3.6" ry="8.5"/>
            <line x1="1.5" y1="10" x2="18.5" y2="10"/>
            <path d="M3 5.5 H17 M3 14.5 H17"/>
          </g>
        </svg>
        <span>www.larkmoorfirm.legal</span>
      </div>
    </footer>
  </main>
</body>
</html>
```